依頼詳細
シュリンクラベルを新しいデザインに変更する目的は、ヘアトリートメントも同じ容器でシリーズとしてのリニューアル新発売します(今までは100mlと少量)ので、2アイテムの関連性とシンプルでいて、新しいデザインで、2本揃えて購入したくなるようなデザイン、バスルームに置いていても、心地よいデザインにしたいからです。容器の素材はPP、 ラベルはシュリンクのPET素材ですから、写真は半透明になりますし、写真ではリアルさを伝えられないので、現在のデザインのように全面に使用しなくても良いと思います、美しい淡い色のグラデか、写真を入れた方が良いのか、他の商品のラベルデザインも参考にしていただきたいです。ロゴは金ホットスタンプを使用してください。
シャンプー1000mlのお徳用サイズは、金ホットスタンプは使用無しでデザインしてください。
記載項目
ラベル:デジタル印刷シュリンク(箔押しアリ) 印刷範囲用データ添付しますから、ここにレイアウトデザインしてください 現在のシャンプー・トリートメント画像も添付します ロゴも添付します 金ホットスタンプ・箔のサイズ: タテ45㎜×ヨコ50㎜ 以内にお願いします
お徳用サイズは、現在のデータを添付します。

希望イメージ
シンプル 複雑
単色 カラフル
暗い 明るい
日常 高級
遊び心 厳粛
未来的 伝統的
女性的 男性的
希望する色
水色系、紫系、金色
納品ファイル
• イラストレーター形式 (.ai)
補足説明
ロゴは、添付のクレイクレンジング・クレイクレンジング・フェイス&ボディソープのロゴに準じてください。今現在のロゴの特に、ラグジュアリーの英字ロゴは、変えてください。トリートメントは、英字のトリートメントは変えないで、現在のを使用しても可能です。
シャンパーニュとヘアトリートメントのそれぞれのテキストデータをイラストレーターで作成しました、添付します。
こちらのテキストを使用してください。
ロゴは、参考にするだけで、TOMIRENOは、クレイクレンジングやクリアクレンジングウォーターと同じにしてください。SHAMPOOやHAIR TREATMENTは新たにデザインご提案してください。
前記の追記の冒頭に「シャンパーニュ」と記載しましたが、「シャンプー」の誤入力です、訂正させていただきます

TMIRENOロゴ・ヘアトリートメントのJANコードを上書きした「text.ai」を添付しますので、こちらで制作をお願いします
参考のために、当社の ①フェイス&ボディソープ  ②クリアクレンジングウォーター  ③クレイクレンジング、 3アイテムの新ラベルデザインを添付ファイル 「ラベルデザイン新シリーズJpg」をご覧いただきますよう、お願いいたします。
このバラの写真のコラージュの色相・明度バリエーションで構成した3点のラベルのイメージに併せるなら、シャンプーのラベルは、香りに使用しているラベンダーやゼラニウムの写真のコラージュのバリエーションが良いのかなと思います。
しかし、個性的過ぎるし、シャンプーは男性も愛用者が多いですので、シンプルにした方が良いのか、どの方向がお客様に喜ばれるか、当社のイメージも考慮しながら、
ご提案くださいますと、ありがたく思います。どうぞ、よろしくお願いいたします。
添付の資料に不備があり、申し訳ありません、締め切りを2日延長いたします。
補足説明です、よろしくお願いいたします。

1.現在のシャンプー商品画像jpgを添付します(容器のポンプの色は白色です)
この容器を シャンプーとトリートメント両方に使用します

2.textのpdfファイルを添付します、.aiファイルが文字化けする場合は、このpdfファイルを見てください

3.シャンプーの香り成分は、天然のラベンダーがメインでゼラニウム(とオレンジ)の香り成分も配合しています

4.トリートメントもシャンプーと同じ香りの予定ですが、ホホバ種子オイルを配合していることも、大きなポイントです
■ 選んだ理由

こちらのデザインは、ベースのグラデーションの色彩、英字フォント、ラベンダーとゼラニウムの画像のコラージュ、全てがブランドイメージを高める素晴らしいデザインだと思います。修正依頼にも快く応じて頂き、ありがとうございました。

■ 提案者全員のお礼・コメント

私の認識不足で、選択のタイミングが遅くなり、申し訳ございませんでした。
ご提案は、いろいろなタイプのデザインがありました。ブランドイメージの幅が広がりました。貴重なご提案を本当にありがとうございました。

```html
<!DOCTYPE html>
<html lang="ja">
<head>
<meta charset="utf-8">
<title>TMIRENO Bath Series Labels</title>
<link href="https://fonts.googleapis.com/css2?family=Cinzel:wght@400&family=Noto+Sans+JP:wght@400;500&family=Noto+Serif+JP:wght@400;500&display=swap" rel="stylesheet">
<style>
  :root {
    --canvas: #eeeeee;
    --ink-light: #ffffff;
    --ink-soft: rgba(255,255,255,0.85);
    --red-hi: #e3262c;
    --red-mid: #b80f16;
    --red-lo: #6e0207;
    --violet-hi: #a463e6;
    --violet-mid: #7434c4;
    --violet-lo: #3c137a;
    --green-hi: #3fb23a;
    --green-mid: #1f8a1d;
    --green-lo: #0a4e0c;
  }
  * { box-sizing: border-box; margin: 0; padding: 0; }
  html, body { width: 1200px; height: 2380px; overflow: hidden; background: var(--canvas); }
  body { position: relative; font-family: "Noto Sans JP", sans-serif; color: var(--ink-light); }

  .label {
    position: absolute; left: 20px; width: 1160px; height: 720px; overflow: hidden;
    box-shadow: 0 4px 14px rgba(0,0,0,0.25);
  }
  .label--shampoo   { top: 20px;   background: radial-gradient(ellipse at 65% 40%, var(--red-hi), var(--red-mid) 55%, var(--red-lo)); }
  .label--treatment { top: 830px;  background: radial-gradient(ellipse at 65% 40%, var(--violet-hi), var(--violet-mid) 55%, var(--violet-lo)); }
  .label--luxury    { top: 1640px; background: radial-gradient(ellipse at 65% 40%, var(--green-hi), var(--green-mid) 55%, var(--green-lo)); }

  .label__bands { position: absolute; inset: 0; width: 100%; height: 100%; }

  .label__info {
    position: absolute; left: 42px; top: 34px; width: 360px;
    font-size: 12.5px; line-height: 1.65; color: var(--ink-soft);
  }
  .label__info p { margin-bottom: 14px; }
  .label__info .product-line { font-size: 14px; color: var(--ink-light); margin-bottom: 4px; }
  .label__info dl { display: grid; grid-template-columns: 90px 1fr; column-gap: 10px; font-size: 11.5px; margin-top: 16px; }
  .label__info dt, .label__info dd { margin-bottom: 6px; }

  .label__marks {
    position: absolute; left: 42px; bottom: 36px; display: flex; align-items: center; gap: 16px;
    font-size: 13px;
  }
  .mark { width: 34px; height: 34px; border: 1.5px solid var(--ink-soft); }
  .mark--round { border-radius: 50%; }

  .label__art {
    position: absolute; left: 910px; top: 60px; width: 200px; height: 600px; border-radius: 40px;
  }
  .label--shampoo .label__art   { background: linear-gradient(180deg, #d4101a 0%, #b30b14 25%, #2f7a2a 45%, #1e5e1c 100%); opacity: 0.85; }
  .label--treatment .label__art { background: linear-gradient(180deg, #c5a8e8 0%, #8e6cc4 45%, #7a9b6a 75%, #c9b48a 100%); opacity: 0.8; }
  .label--luxury .label__art    { background: linear-gradient(180deg, #a6d66a 0%, #6fb83c 50%, #3f8a22 100%); opacity: 0.75; }

  .label__brand {
    position: absolute; left: 490px; top: 130px; width: 390px; text-align: center;
    font-family: "Cinzel", serif; font-weight: 400; z-index: 2;
  }
  .brand-name { font-size: 58px; letter-spacing: 4px; line-height: 1; }
  .brand-line { font-size: 30px; letter-spacing: 3px; line-height: 1.25; margin-top: 14px; }

  .label__jp {
    position: absolute; left: 510px; top: 470px; width: 380px;
    font-family: "Noto Serif JP", serif; font-weight: 500; z-index: 2;
  }
  .label__jp .jp-brand { font-size: 20px; letter-spacing: 2px; }
  .label__jp .jp-product { font-size: 28px; letter-spacing: 2px; margin-top: 4px; white-space: nowrap; }
</style>
</head>
<body>

<section class="label label--shampoo">
  <svg class="label__bands" viewBox="0 0 1160 720" preserveAspectRatio="none" aria-hidden="true">
    <polygon points="300,0 720,0 420,720 0,720 0,520" fill="rgba(255,255,255,0.07)"/>
    <polygon points="480,0 1160,0 1160,180 620,720 430,720" fill="rgba(0,0,0,0.10)"/>
    <polygon points="0,250 1160,470 1160,560 0,330" fill="rgba(255,255,255,0.06)"/>
    <path d="M0,420 C380,300 760,600 1160,380" stroke="rgba(255,255,255,0.18)" stroke-width="2" fill="none"/>
  </svg>
  <div class="label__art" role="img" aria-label="赤いバラの一輪の写真"></div>
  <div class="label__info">
    <p>さわやかな天然ラベンダーの香りに包まれながら、髪と頭皮をやさしく洗い上げます。植物由来の洗浄成分が、うるおいを守りながら汚れを落とし、毎日のバスタイムを心地よい時間に変えます。</p>
    <div class="product-line">トミレノ　ナチュラルシャンプー</div>
    <div>内容量 300mL</div>
    <dl>
      <dt>発売元</dt><dd>ミレノ化粧品株式会社<br>東京都港区北町 1-2-3<br>TEL 03-5550-1234</dd>
      <dt>製造販売元</dt><dd>みどり製薬株式会社<br>大阪府中央区南町 4-5-6</dd>
    </dl>
  </div>
  <div class="label__marks"><span>Made in Japan</span><span class="mark mark--round"></span><span class="mark"></span></div>
  <div class="label__brand">
    <div class="brand-name">TMIRENO</div>
    <div class="brand-line">NATURAL<br>SHAMPOO</div>
  </div>
  <div class="label__jp">
    <div class="jp-brand">トミレノ</div>
    <div class="jp-product">ナチュラルシャンプー</div>
  </div>
</section>

<section class="label label--treatment">
  <svg class="label__bands" viewBox="0 0 1160 720" preserveAspectRatio="none" aria-hidden="true">
    <polygon points="300,0 720,0 420,720 0,720 0,520" fill="rgba(255,255,255,0.07)"/>
    <polygon points="480,0 1160,0 1160,180 620,720 430,720" fill="rgba(0,0,0,0.10)"/>
    <polygon points="0,250 1160,470 1160,560 0,330" fill="rgba(255,255,255,0.06)"/>
    <path d="M0,420 C380,300 760,600 1160,380" stroke="rgba(255,255,255,0.18)" stroke-width="2" fill="none"/>
  </svg>
  <div class="label__art" role="img" aria-label="リボンで束ねたラベンダーの花束の写真"></div>
  <div class="label__info">
    <p>天然ホホバ種子オイル配合。シャンプー後の髪にすばやくなじみ、毛先までしっとりまとまる手触りへ導きます。ラベンダーとゼラニウムのやさしい香りが広がり、ゆったりとした気分にさせてくれます。</p>
    <div class="product-line">トミレノ　ヘアトリートメント</div>
    <div>内容量 300g</div>
    <dl>
      <dt>発売元</dt><dd>ミレノ化粧品株式会社<br>東京都港区北町 1-2-3<br>TEL 03-5550-1234</dd>
      <dt>製造販売元</dt><dd>みどり製薬株式会社<br>www.tomireno-bath.jp</dd>
    </dl>
  </div>
  <div class="label__marks"><span>Made in Japan</span><span class="mark mark--round"></span><span class="mark"></span></div>
  <div class="label__brand">
    <div class="brand-name">TMIRENO</div>
    <div class="brand-line">HAIR<br>TREATMENT</div>
  </div>
  <div class="label__jp">
    <div class="jp-brand">トミレノ</div>
    <div class="jp-product">ヘアトリートメント</div>
  </div>
</section>

<section class="label label--luxury">
  <svg class="label__bands" viewBox="0 0 1160 720" preserveAspectRatio="none" aria-hidden="true">
    <polygon points="300,0 720,0 420,720 0,720 0,520" fill="rgba(255,255,255,0.07)"/>
    <polygon points="480,0 1160,0 1160,180 620,720 430,720" fill="rgba(0,0,0,0.10)"/>
    <polygon points="0,250 1160,470 1160,560 0,330" fill="rgba(255,255,255,0.06)"/>
    <path d="M0,420 C380,300 760,600 1160,380" stroke="rgba(255,255,255,0.18)" stroke-width="2" fill="none"/>
  </svg>
  <div class="label__art" role="img" aria-label="ゼラニウムの葉が舞い散るイラスト"></div>
  <div class="label__info">
    <p>植物の恵みをたっぷり詰め込んだぜいたくな一本。豊かな泡が頭皮をすっきり洗い、髪にハリとツヤを与えます。ご家族みんなでお使いいただけるお得な大容量サイズです。</p>
    <div class="product-line">トミレノ　シャンプーラグジュアリー</div>
    <div>内容量 1000mL</div>
    <dl>
      <dt>発売元</dt><dd>ミレノ化粧品株式会社<br>東京都港区北町 1-2-3<br>TEL 03-5550-1234</dd>
    </dl>
  </div>
  <div class="label__marks"><span>Made in Japan</span><span class="mark mark--round"></span><span class="mark"></span></div>
  <div class="label__brand">
    <div class="brand-name">TMIRENO</div>
    <div class="brand-line">SHAMPOO<br>LUXURY</div>
  </div>
  <div class="label__jp">
    <div class="jp-brand">トミレノ</div>
    <div class="jp-product">シャンプーラグジュアリー</div>
  </div>
</section>

</body>
</html>
```